K9 Orbit needs a business card designed

We need a business card designed for K9 Orbit, an expansion of K9 Systems Pty Ltd (www.k9systems.com.au)

We provide high quality professional services for the Australian space industry. Our clients include the Southern Launch Bureau and companies working in the space industry. We identify people with space related skills both locally and internationally who are then contracted by clients to create products and support space launch activities.

Colours to be used:
- Navy blue #000080
- Rocket metallic #8A7F8D
- Platinum #E5E4E2
- Black #000000
- White #FFFFFF

*Front of the card*
I have attached our K9 Orbit logo, which needs to be the main item on the card. The 'Space' text should be placed to the right of the 'K9' part rather than below, similar to the attached K9 Systems card, which this card should match.

If subtext is included, however, it should read ‘Labour Hire • Consultancy • Project Delivery’ rather than the ‘Design • Build • Test • Maintain’ of the K9 Systems card.

A black background (rather than blue background in the K9 Systems card) might be good, with a white pattern as in the K9 Systems card. If colour is used, the logo should be in its standard colours (as provided for the K9 Orbit logo).

*Back of the card*
Include a smaller K9 Orbit logo on the back.

We need the following details for K9 Orbit personnel (as a template for entry):
- Name
- Company Position
- Mobile Number
- Email
- Office Address
- Include the K9 Orbit website: www.k9orbit.com.au

Overall, we'd like to see a design that communicates the adventure of space, professional integrity, and customer service. We look forward to seeing what you can come up with.

Target Market(s)

We provide high quality professional services for the Australian space industry. Our clients include the Southern Launch Bureau and companies working in the space industry.

Contact Information for Business Card

- Name
- Company Position
- Mobile Number
- Email
- Office Address

Requirements
Must have
• See project description.

```html
<!DOCTYPE html>
<html lang="en">
<head>
<meta charset="utf-8">
<title>K9 Orbit Business Card</title>
<link rel="stylesheet" href="https://fonts.googleapis.com/css2?family=Montserrat:wght@400;500;600&family=Open+Sans:wght@400;600;700&display=swap">
<style>
  :root {
    --navy: #1f1f7a;
    --rocket: #8a7f8d;
    --platinum: #e5e4e2;
    --black: #1c1c1c;
    --white: #ffffff;
    --stage: #4d4d4d;
    --ink: #2b2b2b;
    --faint-dark: #262626;
    --faint-light: #ececec;
  }
  * { box-sizing: border-box; margin: 0; padding: 0; }
  html, body { width: 1200px; height: 1021px; overflow: hidden; }
  body {
    background: var(--stage);
    font-family: "Open Sans", sans-serif;
    position: relative;
  }
  .card {
    position: absolute;
    left: 280px;
    width: 640px;
    height: 366px;
    overflow: hidden;
    box-shadow: 0 10px 28px rgba(0,0,0,.35);
  }
  .card--front { top: 110px; background: var(--black); }
  .card--back { top: 530px; background: linear-gradient(135deg, #ffffff 0%, #f2f2f2 100%); }

  .deco-circle {
    position: absolute;
    border-radius: 50%;
  }
  .card--front .deco-circle {
    width: 330px; height: 330px; left: 300px; top: 40px;
    border: 60px solid var(--faint-dark);
  }
  .card--back .deco-circle {
    width: 300px; height: 300px; left: 300px; top: 150px;
    border: 56px solid var(--faint-light);
  }

  .brand { position: absolute; }
  .brand__name {
    font-family: "Montserrat", sans-serif;
    font-weight: 600;
    letter-spacing: 0.18em;
    white-space: nowrap;
  }
  .brand__tagline {
    font-family: "Montserrat", sans-serif;
    font-weight: 500;
    white-space: nowrap;
    letter-spacing: 0.02em;
  }

  .card--front .brand { left: 150px; top: 140px; }
  .card--front .brand__name { color: var(--white); font-size: 46px; }
  .card--front .brand__tagline { color: var(--platinum); font-size: 12.5px; margin-top: 4px; padding-left: 120px; }

  .card--back .brand { left: 40px; top: 34px; }
  .card--back .brand__name { color: var(--navy); font-size: 36px; }
  .card--back .brand__tagline { color: var(--rocket); font-size: 10.5px; margin-top: 2px; padding-left: 92px; }

  .contact {
    position: absolute;
    left: 40px; top: 190px;
    color: var(--ink);
    font-size: 15px;
    line-height: 1.3;
  }
  .contact__address { margin-bottom: 12px; }
  .contact__row { display: flex; align-items: center; gap: 7px; }
  .contact__row svg { width: 14px; height: 14px; flex: none; }

  .person {
    position: absolute;
    right: 46px; top: 268px;
    text-align: right;
  }
  .person__name { color: var(--navy); font-weight: 700; font-size: 20px; }
  .person__role { color: var(--ink); font-size: 16px; }
</style>
</head>
<body>
  <section class="card card--front" aria-label="Card front">
    <div class="deco-circle"></div>
    <div class="brand">
      <div class="brand__name">K9 Orbit</div>
      <div class="brand__tagline">Labour Hire • Consultancy • Project Delivery</div>
    </div>
  </section>

  <section class="card card--back" aria-label="Card back">
    <div class="deco-circle"></div>
    <div class="brand">
      <div class="brand__name">K9 Orbit</div>
      <div class="brand__tagline">Labour Hire • Consultancy • Project Delivery</div>
    </div>

    <div class="contact">
      <div class="contact__address">57 N. W. 4th Street<br>Tampa, Florida, 33602</div>
      <div class="contact__row">
        <svg viewBox="0 0 14 14" fill="none" stroke="#1f1f7a" stroke-width="1.3"><rect x="3.5" y="1" width="7" height="12" rx="1.3"/><line x1="6" y1="11" x2="8" y2="11"/></svg>
        <span>(321) 555-0148</span>
      </div>
      <div class="contact__row">
        <svg viewBox="0 0 14 14" fill="none" stroke="#1f1f7a" stroke-width="1.3"><rect x="1" y="3" width="12" height="8.5"/><polyline points="1,3 7,8 13,3"/></svg>
        <span>daniel@k9orbit.com.au</span>
      </div>
      <div class="contact__row">
        <svg viewBox="0 0 14 14" fill="none" stroke="#1f1f7a" stroke-width="1.2"><circle cx="7" cy="7" r="5.8"/><ellipse cx="7" cy="7" rx="2.6" ry="5.8"/><line x1="1.2" y1="7" x2="12.8" y2="7"/></svg>
        <span>www.k9orbit.com.au</span>
      </div>
    </div>

    <div class="person">
      <div class="person__name">Daniel Harper</div>
      <div class="person__role">President</div>
    </div>
  </section>
</body>
</html>
```